Lorne Hollow Farm Postcard Design

I am looking for a new postcard design to mail out this season. We are a Farm business that does wholesale and retail and bulk seasoned firewood sales. we sell firewood from anything from bagged wood to tractor trailer loads of wood. We sell firewood in bulk bags. Pick up or delivery available there is no order to big or too small. I need my business name and phone number on the cards Lorne Hollow Farm 848-316-0572 (call or text) I would like it to say we are the best priced guaranteed. I want something that is simple and straight forward but also really catches the eye when they see these in the mail box. I attached my logo and feel free to use photos of split firewood if you would like. id like my email on the card Lornehollowfarm90@mailvista.net.

Target Market(s)

Firewood purchasers

Industry/Entity Type

agriculture

Requirements
Must have
• email phone number logo

```html
<!DOCTYPE html>
<html lang="en">
<head>
<meta charset="utf-8">
<title>Lorne Hollow Farm – Firewood Postcard</title>
<link rel="stylesheet" href="https://fonts.googleapis.com/css2?family=Archivo:wght@700;800;900&family=Lexend:wght@400;500&display=swap">
<style>
  :root{
    --orange:#E8571E;
    --brown:#7A5240;
    --yellow:#FDD22A;
    --black:#050505;
    --white:#ffffff;
    --ink:#2a1a10;
    --tick:#2E9B3A;
  }
  *{margin:0;padding:0;box-sizing:border-box}
  html,body{width:848px;height:1200px;overflow:hidden;background:var(--orange)}
  .postcard{position:relative;width:848px;height:1200px;overflow:hidden;font-family:"Archivo",Arial,sans-serif}
  .backdrop{position:absolute;inset:0}
  .top-phone{position:absolute;right:76px;top:40px;color:var(--white);font-weight:800;font-size:27px;letter-spacing:.3px}
  .brand-box{position:absolute;left:86px;top:53px;width:188px;height:162px;background:var(--black);border-radius:14px;display:flex;align-items:center;justify-content:center;gap:10px;padding:12px}
  .brand-mark{width:14px;height:14px;background:var(--yellow);flex:none}
  .brand-name{color:var(--yellow);font-weight:800;font-size:23px;line-height:1.15;text-align:left}
  .headline{position:absolute;left:85px;top:252px;color:var(--white);font-weight:900;font-size:52px;line-height:61px;letter-spacing:.5px;text-shadow:2px 3px 0 var(--orange)}
  .services{position:absolute;left:60px;top:769px;width:735px;height:224px;background:var(--black);border:1.5px solid var(--yellow);border-radius:10px}
  .services-tab{position:absolute;left:115px;top:755px;width:191px;height:43px;background:var(--yellow);border-radius:8px;display:flex;align-items:center;justify-content:center;font-weight:800;font-size:20px;color:var(--black)}
  .service-list{position:absolute;list-style:none;font-family:"Lexend",Arial,sans-serif;font-size:20px;color:var(--white);letter-spacing:.6px}
  .service-list li{height:37px;display:flex;align-items:center;gap:11px}
  .service-list.left{left:115px;top:824px}
  .service-list.right{left:454px;top:824px}
  .tick{width:18px;height:18px;flex:none}
  .price-box{position:absolute;left:60px;top:1013px;width:135px;height:125px;background:var(--yellow);border-radius:8px;box-shadow:4px 4px 0 #1f4d1a;text-align:center}
  .price-label{position:absolute;left:7px;top:4px;width:120px;height:36px;background:var(--orange);border-radius:8px;color:var(--white);font-weight:800;font-size:17px;display:flex;align-items:center;justify-content:center}
  .price-amount{position:absolute;left:0;right:0;top:44px;font-weight:900;font-size:43px;color:var(--black);letter-spacing:-1px}
  .price-unit{position:absolute;left:0;right:0;top:97px;font-weight:800;font-size:17px;color:var(--black)}
  .guarantee{position:absolute;left:195px;top:1041px;width:278px;height:82px;background:var(--black);border:1.5px solid var(--yellow);border-left:none;border-radius:0 8px 8px 0;box-shadow:6px 6px 0 var(--orange);color:var(--white);font-weight:800;font-size:20px;display:flex;align-items:center;padding-left:16px}
  .contact{position:absolute;left:513px;top:1044px;width:277px;height:83px;background:var(--black);border:1.5px solid var(--yellow);border-radius:8px;box-shadow:4px 6px 0 var(--orange);color:var(--white)}
  .contact-icon{position:absolute;left:20px;top:24px;width:32px;height:32px}
  .contact-label{position:absolute;left:65px;top:14px;font-family:"Lexend",Arial,sans-serif;font-size:15px;letter-spacing:.3px}
  .contact-phone{position:absolute;left:64px;top:36px;font-weight:800;font-size:26px}
  .footer-details{position:absolute;left:0;right:0;top:1164px;display:flex;justify-content:center;gap:28px;padding-left:30px;font-weight:800;font-size:13.5px;color:var(--ink)}
</style>
</head>
<body>
<main class="postcard">
  <svg class="backdrop" width="848" height="1200" viewBox="0 0 848 1200" xmlns="http://www.w3.org/2000/svg">
    <defs>
      <linearGradient id="woodTone" x1="0" y1="0" x2="1" y2="1">
        <stop offset="0" stop-color="#4a3a2a"/>
        <stop offset=".35" stop-color="#a88460"/>
        <stop offset=".7" stop-color="#c9a77f"/>
        <stop offset="1" stop-color="#6f5238"/>
      </linearGradient>
      <linearGradient id="yardTone" x1="0" y1="0" x2="1" y2="0">
        <stop offset="0" stop-color="#d9dbdc"/>
        <stop offset=".45" stop-color="#8a8a86"/>
        <stop offset=".8" stop-color="#5a1f22"/>
        <stop offset="1" stop-color="#6f8a58"/>
      </linearGradient>
    </defs>
    <rect width="848" height="1200" fill="var(--orange)"/>
    <rect y="720" width="848" height="480" fill="url(#yardTone)" role="img" aria-label="Photo of a firewood delivery truck parked beside a garage"/>
    <path d="M0,0 H848 V810 H795 V740 H0 Z" fill="var(--orange)"/>
    <path d="M0,680 C260,760 620,760 848,560 V600 C660,745 320,760 0,715 Z" fill="var(--yellow)"/>
    <path d="M0,225 C140,95 380,65 600,72 C720,78 800,120 848,150 V565 C720,680 480,700 260,688 C140,682 60,660 0,628 Z" fill="url(#woodTone)" role="img" aria-label="Photo of a large stack of split seasoned firewood on a wooden rack"/>
    <path d="M0,180 C170,40 470,0 848,135 V160 C620,70 330,50 0,240 Z" fill="var(--brown)"/>
    <path d="M848,560 C700,690 440,705 180,690 C420,680 690,650 848,500 Z" fill="var(--brown)"/>
    <path d="M95,1200 V1175 Q95,1155 120,1155 H740 Q765,1155 765,1175 V1200 Z" fill="var(--yellow)"/>
    <rect y="1185" width="848" height="15" fill="var(--yellow)"/>
  </svg>

  <div class="top-phone">+848-316-0572</div>

  <div class="brand-box">
    <span class="brand-mark"></span>
    <span class="brand-name">Lorne<br>Hollow<br>Farm</span>
  </div>

  <h1 class="headline">PREMIUM SPLIT<br>SEASONED<br>FIREWOOD<br>FOR YOUR<br>HOME OR BUSINESS</h1>

  <section class="services"></section>
  <div class="services-tab">What We Do?</div>
  <ul class="service-list left">
    <li><svg class="tick" viewBox="0 0 20 20"><circle cx="10" cy="10" r="10" fill="var(--yellow)"/><path d="M5.5 10.3l3 3 6-6.3" fill="none" stroke="var(--tick)" stroke-width="2.4" stroke-linecap="round" stroke-linejoin="round"/></svg>Wholesale</li>
    <li><svg class="tick" viewBox="0 0 20 20"><circle cx="10" cy="10" r="10" fill="var(--yellow)"/><path d="M5.5 10.3l3 3 6-6.3" fill="none" stroke="var(--tick)" stroke-width="2.4" stroke-linecap="round" stroke-linejoin="round"/></svg>Bulk</li>
    <li><svg class="tick" viewBox="0 0 20 20"><circle cx="10" cy="10" r="10" fill="var(--yellow)"/><path d="M5.5 10.3l3 3 6-6.3" fill="none" stroke="var(--tick)" stroke-width="2.4" stroke-linecap="round" stroke-linejoin="round"/></svg>Bagged Wood</li>
    <li><svg class="tick" viewBox="0 0 20 20"><circle cx="10" cy="10" r="10" fill="var(--yellow)"/><path d="M5.5 10.3l3 3 6-6.3" fill="none" stroke="var(--tick)" stroke-width="2.4" stroke-linecap="round" stroke-linejoin="round"/></svg>Seasoned</li>
  </ul>
  <ul class="service-list right">
    <li><svg class="tick" viewBox="0 0 20 20"><circle cx="10" cy="10" r="10" fill="var(--yellow)"/><path d="M5.5 10.3l3 3 6-6.3" fill="none" stroke="var(--tick)" stroke-width="2.4" stroke-linecap="round" stroke-linejoin="round"/></svg>Retail</li>
    <li><svg class="tick" viewBox="0 0 20 20"><circle cx="10" cy="10" r="10" fill="var(--yellow)"/><path d="M5.5 10.3l3 3 6-6.3" fill="none" stroke="var(--tick)" stroke-width="2.4" stroke-linecap="round" stroke-linejoin="round"/></svg>Delivery Available</li>
    <li><svg class="tick" viewBox="0 0 20 20"><circle cx="10" cy="10" r="10" fill="var(--yellow)"/><path d="M5.5 10.3l3 3 6-6.3" fill="none" stroke="var(--tick)" stroke-width="2.4" stroke-linecap="round" stroke-linejoin="round"/></svg>Eco-Friendly</li>
    <li><svg class="tick" viewBox="0 0 20 20"><circle cx="10" cy="10" r="10" fill="var(--yellow)"/><path d="M5.5 10.3l3 3 6-6.3" fill="none" stroke="var(--tick)" stroke-width="2.4" stroke-linecap="round" stroke-linejoin="round"/></svg>Premium Quality</li>
  </ul>

  <div class="guarantee">Best Priced Guaranteed</div>
  <div class="price-box">
    <div class="price-label">Starts at</div>
    <div class="price-amount">$500</div>
    <div class="price-unit">/Order</div>
  </div>

  <div class="contact">
    <svg class="contact-icon" viewBox="0 0 24 24"><path fill="var(--white)" d="M6.6 10.8a15.1 15.1 0 0 0 6.6 6.6l2.2-2.2a1 1 0 0 1 1-.25 11.4 11.4 0 0 0 3.6.57 1 1 0 0 1 1 1V20a1 1 0 0 1-1 1A17 17 0 0 1 3 4a1 1 0 0 1 1-1h3.5a1 1 0 0 1 1 1c0 1.25.2 2.45.57 3.6a1 1 0 0 1-.25 1z"/></svg>
    <div class="contact-label">Contact Us Now!</div>
    <div class="contact-phone">+848-316-0572</div>
  </div>

  <footer class="footer-details">
    <span>Lornehollowfarm90@mailvista.net</span>
    <span>90 Ridgeway Rd Millbrook NJ 07799</span>
  </footer>
</main>
</body>
</html>
```